Build Distinctive Business Card: Public Relations Government Relations firm

I have logo and colors done (attached) need a very cool way to present it on a business card (can be two sided if need be).

Public Relations Government Relations firm

Info:

Marcus Teller, CEO
Harbor Public Relations
2736 West Larkmont Blvd.
Los Angeles CA 90012
(o) 213.555.0148
(f) 213.555.0193
marcus@harborhpr-example.com

Target Market(s)

Government relations, public relations, lobbyist, I was a past State Senator

Industry/Entity Type

Business

Contact Information for Business Card

Info:

Marcus Teller, CEO
Harbor Public Relations
2736 West Larkmont Blvd.
Los Angeles CA 90012
(o) 213.555.0148
(f) 213.555.0193
marcus@harborhpr-example.com
@marcusteller

Requirements
Must have
• A sense of balance given logo is already done.
• It's a government relations firm really.
• Lobbyist type.
• Senatorial type...

```html
<!DOCTYPE html>
<html lang="en">
<head>
<meta charset="utf-8">
<title>Harbor Public Relations — Business Card</title>
<link rel="stylesheet" href="https://fonts.googleapis.com/css2?family=Arimo:wght@400;700&display=swap">
<style>
  :root {
    --backdrop: #0a2147;
    --brand-blue: #0061b8;
    --brand-deep: #00509e;
    --card-white: #ffffff;
    --ink: #111111;
  }
  * { margin: 0; padding: 0; box-sizing: border-box; }
  html, body {
    width: 1200px;
    height: 1000px;
    overflow: hidden;
    background: var(--backdrop);
    font-family: "Arimo", Arial, sans-serif;
  }
  .card {
    position: absolute;
    width: 612px;
    height: 359px;
  }
  .card-front {
    left: 293px;
    top: 123px;
    background: var(--brand-blue);
    display: flex;
    align-items: center;
    justify-content: center;
  }
  .card-back {
    left: 294px;
    top: 517px;
    background: var(--card-white);
    color: var(--ink);
  }
  .front-mark {
    display: flex;
    align-items: center;
    gap: 18px;
  }
  .front-mark .dot {
    width: 64px;
    height: 64px;
    border-radius: 50%;
    background: var(--card-white);
  }
  .front-mark .wordmark {
    color: var(--card-white);
    font-size: 46px;
    font-weight: 700;
  }
  .back-mark {
    position: absolute;
    left: 24px;
    top: 34px;
    display: flex;
    align-items: center;
    gap: 14px;
  }
  .back-mark .dot {
    width: 108px;
    height: 108px;
    border-radius: 50%;
    background: var(--brand-deep);
  }
  .back-mark .wordmark {
    color: var(--brand-deep);
    font-size: 30px;
    font-weight: 700;
  }
  .contact {
    position: absolute;
    right: 22px;
    top: 160px;
    text-align: right;
    font-size: 15px;
    line-height: 20px;
  }
  .contact .name {
    font-size: 19px;
    line-height: 24px;
  }
  .contact .name strong { font-weight: 700; }
  .contact .role { margin-bottom: 18px; }
  .contact .address { line-height: 21px; margin-bottom: 4px; }
  .contact .email { margin-top: 5px; }
  .contact .label { margin-right: 8px; }
</style>
</head>
<body>
  <section class="card card-front">
    <div class="front-mark">
      <span class="dot"></span>
      <span class="wordmark">Harbor</span>
    </div>
  </section>

  <section class="card card-back">
    <div class="back-mark">
      <span class="dot"></span>
      <span class="wordmark">Harbor Public Relations</span>
    </div>
    <div class="contact">
      <p class="name">Marcus <strong>Teller</strong></p>
      <p class="role">CEO</p>
      <p class="address">2736 West Larkmont Blvd.<br>Los Angeles CA 90012</p>
      <p><span class="label">T:</span>213.555.0148</p>
      <p><span class="label">F:</span>213.555.0193</p>
      <p class="email"><span class="label">E:</span>marcus@harborhpr-example.com</p>
    </div>
  </section>
</body>
</html>
```